Epoxy Flooring Contractor business card

We need a business card to promote a new addition to our business. We now offer Epoxy Flooring. We would like for the business card to include the images attached. One is our logo, the other is a sample of metallic epoxy flooring, we would like to incorporate that somewhere into the design. I was thinking an icon of a man pushing a concrete grinder and have the color set to the metallic epoxy color. I found a business card sample on this website, I will attach it. It has the icon that we are looking for, or something similar.
Our company name is Brightmore Coatings LLC
Our owners name is Dana Pellow
Phone is 561-847-2916
website is www.brightmore-coatingsllc.com
please let me know if you need any other info

Contact Information for Business Card

Brightmore Coatings LLC
Dana Pellow, owner
Phone: 561-847-2916
Address: P.O Box 8146 Lake Worth, FL 33471
www.Brightmore-CoatingsLLC.com
BrightmoreCoatingsLLC@mailvista.net
Include logo attached
It must include a Clip art of man with concrete grinder
Must include metallic epoxy design attached
Must include the following text
Residential Garage Flooring
Epoxy Countertops
Commercial Epoxy Flooring
Restaurant Flooring
Warehouse Flooring
Licensed & Insured
Free Estimates

Colors

Designer to choose colors to be used in the design.

Requirements
Must have
• Include logo attached
• It must include a Clip art of man with concrete grinder
• Must include metallic epoxy design attached
• Must include the following text
• Garage Epoxy Flooring
• Residential Epoxy Flooring
• Concrete Floor Crack Repairs
• Concrete Floor Grinding
• Commercial & Warehouse Epoxy Flooring
• Restaurant Epoxy Flooring
• Epoxy Countertops
• Non Slip Epoxy Pool Decks
• Textured Finishes, Flakes, Granite Coat, Metallic & Quartz
• FREE ESTIMATES • LICENSED & INSURED

```html
<!DOCTYPE html>
<html lang="en">
<head>
<meta charset="utf-8">
<title>Brightmore Coatings – Business Card</title>
<link href="https://fonts.googleapis.com/css2?family=Roboto:wght@400;500&display=swap" rel="stylesheet">
<style>
  :root {
    --backdrop: #0f0f10;
    --card: #1c1c1d;
    --card-edge: #262627;
    --silver: #cfcfcf;
    --silver-soft: #a9a9a9;
    --rule: #9a9a9a;
  }
  * { margin: 0; padding: 0; box-sizing: border-box; }
  html, body {
    width: 1200px; height: 900px; overflow: hidden;
    background: var(--backdrop);
    font-family: "Roboto", Arial, sans-serif;
    color: var(--silver);
  }
  .canvas {
    width: 1200px; height: 900px;
    display: flex; flex-direction: column;
    align-items: center; justify-content: center; gap: 36px;
  }
  .card {
    width: 700px; height: 400px;
    background: linear-gradient(135deg, var(--card) 0%, var(--card-edge) 70%, var(--card) 100%);
    position: relative;
  }
  .brand {
    display: flex; align-items: center; gap: 14px;
  }
  .brand-square {
    width: 34px; height: 34px; background: var(--silver);
  }
  .brand-name {
    font-weight: 500; font-size: 30px; letter-spacing: 1.5px;
    line-height: 1.1; color: var(--silver);
  }

  /* Front */
  .card-front {
    display: flex; flex-direction: column; align-items: center; justify-content: center; gap: 40px;
  }
  .services {
    text-align: center; font-size: 16px; line-height: 1.55;
    letter-spacing: 1px; color: var(--silver-soft);
  }

  /* Back */
  .card-back {
    display: flex; align-items: center; padding: 0 56px;
  }
  .card-back .brand { width: 270px; }
  .card-back .brand-name { font-size: 26px; }
  .divider {
    width: 1px; height: 200px; background: var(--rule); margin: 0 34px 0 30px;
  }
  .contact { font-size: 17px; color: var(--silver-soft); }
  .person-name {
    font-size: 34px; font-weight: 500; letter-spacing: 1px; color: var(--silver);
  }
  .person-role { font-size: 16px; margin: 2px 0 14px; }
  .address { line-height: 1.35; margin-bottom: 14px; }
  .contact-line {
    display: flex; align-items: center; gap: 10px; line-height: 1.5;
  }
  .contact-line svg { width: 14px; height: 14px; flex: none; }
</style>
</head>
<body>
<main class="canvas">

  <section class="card card-front">
    <div class="brand">
      <span class="brand-square"></span>
      <span class="brand-name">Brightmore Coatings</span>
    </div>
    <p class="services">
      Residential Garage Flooring | Epoxy Countertops<br>
      Commercial Epoxy Flooring | Restaurant Flooring<br>
      Warehouse Flooring | Licensed &amp; Insured | Free Estimates
    </p>
  </section>

  <section class="card card-back">
    <div class="brand">
      <span class="brand-square"></span>
      <span class="brand-name">Brightmore<br>Coatings</span>
    </div>
    <span class="divider"></span>
    <div class="contact">
      <h1 class="person-name">DANA PELLOW</h1>
      <p class="person-role">Owner</p>
      <p class="address">P.O Box 8146 Lake<br>Worth, FL 33471</p>
      <p class="contact-line">
        <svg viewBox="0 0 16 16" aria-hidden="true"><path fill="currentColor" d="M4 1l2.5 3-1.5 1.8c.8 1.8 2.4 3.4 4.2 4.2L11 8.5l3 2.5-1.5 3C7 14 2 9 2 3.5z"/></svg>
        561-847-2916
      </p>
      <p class="contact-line">
        <svg viewBox="0 0 16 16" aria-hidden="true"><rect x="1.5" y="3.5" width="13" height="9" fill="none" stroke="currentColor" stroke-width="1.3"/><path d="M1.5 3.5L8 9l6.5-5.5" fill="none" stroke="currentColor" stroke-width="1.3"/></svg>
        BrightmoreCoatingsLLC@mailvista.net
      </p>
      <p class="contact-line">
        <svg viewBox="0 0 16 16" aria-hidden="true"><circle cx="8" cy="8" r="6.3" fill="none" stroke="currentColor" stroke-width="1.2"/><ellipse cx="8" cy="8" rx="2.7" ry="6.3" fill="none" stroke="currentColor" stroke-width="1.2"/><path d="M1.7 8h12.6" stroke="currentColor" stroke-width="1.2"/></svg>
        www.Brightmore-CoatingsLLC.com
      </p>
    </div>
  </section>

</main>
</body>
</html>
```